Packaging design - PROTEIN BALLS

PACKAGING
The packaging is a round carton roll, size: Ø73x180 mm, mockup sample enclosed, The label on the carton roll should have a size of 225x178 mm (width x height)

PRODUCT
Chrunchy, cheesy PROTEIN BALLS (100% pure cheese) with a huge amount of protein (65%), a lot of calcium and very low carbogydrates (3%). Diameter about 1.5 cm.

DESIGN
Since our customers are very sporty people, runner, bodybuilder, etc. The design must fit to this sporty customer segment.

FILES
We need the open data for InDesign with all fonts and pictures. If there are licenses tu buy, we will do it.

SUMMARY
1. SNACK
• Crunchy cheese balls with a diameter of about 1.5cm
• 3 different flavors: "Swiss Alpine Salt", "Provencale" and "Hot Chili"
• High in Protein (65%) and Calcium (2%)
• Low in carbohydrates (3%)

2. PACKAGING
• Carton roll, size: Ø73x180 mm
• Background can be every color, but we think a black one will be high premium.
• Maybe different sports are represented in the background, maybe also cheese
• Be creative
• Label applied, size: 225x178 mm

3. DESIGN
• Product name = (Cheese) PROTEIN BALLS
• 3 different colors for the 3 flavors "Swiss Alpine Salt", "Provencale" and "Hot Chili"
• HighProtein, High Calcium and LowCarb must be pointed out on the front
• Swissness: Swiss made must be pointed out
• fresh and young design, most customers are sporty people, pumper with a strong body awareness

Target Market(s)

TARGET CUSTOMER
Our main customers are extremely sporty people, who work very hard on their muscles and fitness, most of them are runners, cross fitnesser, bodybuilders, etc We will launch the product in fitness centers, in supplement shops and we are planning to make some stories with sporty influencer.

Font styles to use
Serif
Sans Serif

Requirements
Must have
• Cheese, naturalness, healthy, PROTEIN balls, muscles, Swissness must showed on the product.

```html
<!DOCTYPE html>
<html lang="en">
<head>
<meta charset="utf-8">
<title>Cheesy Protein Balls – Flavour Labels</title>
<link href="https://fonts.googleapis.com/css2?family=Exo+2:ital,wght@1,900&family=Saira+Condensed:wght@500;600&display=swap" rel="stylesheet">
<style>
  :root {
    --page: #ececec;
    --kraft: #e2d3b6;
    --kraft-dark: #d6c5a3;
    --ink: #163848;
    --cream: #eadbbb;
    --flavour-ink: #6d665a;
    --chili: #dc4a22;
    --provencale: #e9a41c;
    --alpine: #13959a;
    --swiss-red: #d2202a;
    --ball-light: #d9bd8a;
    --ball-dark: #a9895a;
  }
  * { box-sizing: border-box; margin: 0; padding: 0; }
  html, body { width: 1200px; height: 882px; overflow: hidden; }
  body {
    background: var(--page);
    font-family: "Saira Condensed", "Arial Narrow", sans-serif;
    position: relative;
  }
  .label {
    position: absolute;
    top: 88px;
    width: 243px;
    height: 705px;
    background: linear-gradient(180deg, var(--kraft), var(--kraft-dark));
    overflow: hidden;
  }
  .label--chili { left: 188px; --flavour: var(--chili); }
  .label--provencale { left: 474px; --flavour: var(--provencale); }
  .label--alpine { left: 759px; --flavour: var(--alpine); }

  .label__panel { position: absolute; left: 0; top: 0; width: 243px; height: 570px; }
  .label__panel path { fill: var(--flavour); }

  .claims {
    position: absolute; left: 28px; top: 18px;
    list-style: none; color: var(--ink);
    font-weight: 600; font-size: 18px; line-height: 28px;
  }
  .claims li::before {
    content: ""; display: inline-block; width: 8px; height: 8px;
    background: var(--ink); margin-right: 10px; vertical-align: 2px;
  }
  .hero {
    position: absolute; left: 0; top: 116px; width: 182px; height: 206px;
    background: linear-gradient(160deg, #1e4150, #12303c);
    border-radius: 0 60px 30px 0;
    opacity: .92;
  }
  .ball {
    position: absolute; left: 32px; top: 326px; width: 90px; height: 86px;
    border-radius: 50%;
    background: radial-gradient(circle at 40% 35%, var(--ball-light), var(--ball-dark));
  }
  .title {
    position: absolute; color: var(--cream);
    font-family: "Exo 2", "Arial Black", sans-serif; font-style: italic; font-weight: 900;
    writing-mode: vertical-rl; transform: rotate(180deg);
    line-height: 1; white-space: nowrap;
  }
  .title--cheesy { left: 132px; top: 232px; font-size: 40px; }
  .title--main { left: 180px; top: 36px; font-size: 44px; letter-spacing: 1px; }

  .facts {
    position: absolute; left: 32px; color: var(--ink);
    font-weight: 600; font-size: 17px; line-height: 19px; text-transform: uppercase;
  }
  .facts--high { top: 418px; }
  .facts--low { top: 494px; }

  .flavour {
    position: absolute; left: 32px; top: 590px; color: var(--flavour-ink);
    font-weight: 600; font-size: 28px; line-height: 29px; text-transform: uppercase;
  }
  .origin-mark {
    position: absolute; left: 158px; top: 660px; width: 28px; height: 28px;
    background: var(--swiss-red);
  }
</style>
</head>
<body>

<section class="label label--chili">
  <svg class="label__panel" viewBox="0 0 243 570"><path d="M0 0H243V528C243 552 225 570 200 570H0Z"/></svg>
  <ul class="claims"><li>HighProtein</li><li>High Calcium</li><li>Low Carb</li></ul>
  <div class="hero" role="img" aria-label="Illustration of a flexing bodybuilder"></div>
  <div class="ball" role="img" aria-label="Photo of a hot chili cheese protein ball"></div>
  <div class="title title--cheesy">Cheesy</div>
  <div class="title title--main">PROTEIN BALLS</div>
  <p class="facts facts--high">High in<br>protein (65%)<br>and calcium (2%)</p>
  <p class="facts facts--low">Low in<br>carbohydrates<br>(3%)</p>
  <p class="flavour">Hot Chili</p>
  <div class="origin-mark"></div>
</section>

<section class="label label--provencale">
  <svg class="label__panel" viewBox="0 0 243 570"><path d="M0 0H243V528C243 552 225 570 200 570H0Z"/></svg>
  <ul class="claims"><li>HighProtein</li><li>High Calcium</li><li>Low Carb</li></ul>
  <div class="hero" role="img" aria-label="Illustration of a flexing bodybuilder"></div>
  <div class="ball" role="img" aria-label="Photo of a provencale cheese protein ball"></div>
  <div class="title title--cheesy">Cheesy</div>
  <div class="title title--main">PROTEIN BALLS</div>
  <p class="facts facts--high">High in<br>protein (65%)<br>and calcium (2%)</p>
  <p class="facts facts--low">Low in<br>carbohydrates<br>(3%)</p>
  <p class="flavour">Provencale</p>
  <div class="origin-mark"></div>
</section>

<section class="label label--alpine">
  <svg class="label__panel" viewBox="0 0 243 570"><path d="M0 0H243V528C243 552 225 570 200 570H0Z"/></svg>
  <ul class="claims"><li>HighProtein</li><li>High Calcium</li><li>Low Carb</li></ul>
  <div class="hero" role="img" aria-label="Illustration of a flexing bodybuilder"></div>
  <div class="ball" role="img" aria-label="Photo of a Swiss alpine salt cheese protein ball"></div>
  <div class="title title--cheesy">Cheesy</div>
  <div class="title title--main">PROTEIN BALLS</div>
  <p class="facts facts--high">High in<br>protein (65%)<br>and calcium (2%)</p>
  <p class="facts facts--low">Low in<br>carbohydrates<br>(3%)</p>
  <p class="flavour">Swiss Alpine<br>Salt</p>
  <div class="origin-mark"></div>
</section>

</body>
</html>
```